Financial Planning Design Client Brochure

Dear Designers,

My business is MORVAN Financial which provides financial planning advice to 20-80 year old individuals and small to medium businesses. MORVAN Financial provides financial planning advice in the following areas:

- General Financial Planning
- Superannuation (retirement saving structure)
- Retirement Planning
- Life Insurances (Risk Management)
- Education Funding
- Tax Planning
- Wealth Creation
- Ongoing advice (keeping clients on track)

The brochure will be given to new/prospective clients so essentially will be a marketing document. It will generally be inserted within a MORVAN Financial folder (please see attached photos). Therefore the brochure is going to obviously have to be aligned with the style and current theme/design of this folder. Please see our website which is a little outdated, however it provides a general further insight into our business www.morvanfinancial-example.com.au.

I have attached the wording for the brochure under "MORVAN Financial brochure". In addition there is an outdated diagram under "Services we provide" that I would like re-done. I am open to all ideas and formats to suit this brochure as its fairly simplistic.

Within the brochure, please use as many photo's or images you feel important to support the financial planning theme throughout the brochure.

I would like to use an A3 page that will be folded in half to A4 and have attached an example from our printer. It will be printed most probably on 250gsm quality. Also, will you be providing press ready formats? The colour for MORVAN Financial is as follows:

#00adef

R: 0
G: 173
B: 239

I have attached the current logos in jpeg and EPS format. If you cannot access the EPS files from my uploaded files below, please let me know and I can email them to you.

Many thanks
Brett.

Target Market(s)

It will essentially be high earning professionals between the age of 35-50. Half of this target market will have children or be married

Industry/Entity Type

Financial

Requirements
Must have
• Compliement the folder it will be inserted within.

```html
<!DOCTYPE html>
<html lang="en">
<head>
<meta charset="utf-8">
<title>MORVAN Financial – Client Brochure Spread</title>
<link rel="stylesheet" href="https://fonts.googleapis.com/css2?family=Open+Sans:wght@300;400;600;700&display=swap">
<style>
  :root {
    --brand-blue: #00adef;
    --brand-navy: #1d2b4a;
    --paper: #ffffff;
    --page-edge: #e4e6ea;
    --body-text: #5a5f66;
    --backdrop: #202124;
  }
  * { box-sizing: border-box; margin: 0; padding: 0; }
  html, body {
    width: 1200px; height: 900px; overflow: hidden;
    background: var(--backdrop);
    font-family: "Open Sans", Arial, sans-serif;
  }
  .spread {
    position: absolute; left: 34px; top: 50px;
    width: 1132px; height: 800px;
    display: flex;
  }
  .page {
    position: relative; width: 566px; height: 800px;
    background: var(--paper); overflow: hidden;
  }
  .page--left { border-right: 1px solid var(--page-edge); }

  .photo { position: absolute; }
  .photo--family {
    left: 140px; top: 40px; width: 390px; height: 245px;
    background: linear-gradient(135deg, #d9c3ad 0%, #e9ddd0 45%, #9eb3c4 100%);
  }
  .welcome-title {
    position: absolute; left: 26px; top: 40px; height: 330px;
    writing-mode: vertical-rl; transform: rotate(180deg);
    white-space: nowrap;
  }
  .welcome-title h1 {
    font-weight: 300; font-size: 52px; line-height: 1;
    color: var(--brand-blue); letter-spacing: -1px;
  }
  .welcome-title .brand-lockup {
    margin-left: 8px;
    font-weight: 400; font-size: 16px; line-height: 1.05;
    color: var(--brand-navy);
  }
  .welcome-body {
    position: absolute; left: 40px; top: 392px; width: 490px;
    font-size: 11.5px; line-height: 1.75; color: var(--body-text);
  }
  .welcome-body p { margin-bottom: 12px; }
  .welcome-body .brand-name { color: var(--brand-blue); font-weight: 600; }
  .photo--handshake {
    float: right; width: 200px; height: 165px;
    margin: 4px -4px 8px 16px; position: relative;
    background: linear-gradient(135deg, #c9ccd3 0%, #e8e6e2 50%, #3b4252 100%);
  }

  .operate-band {
    position: absolute; left: 0; top: 62px; width: 526px; height: 72px;
    background: var(--brand-blue);
    display: flex; align-items: center; padding-left: 40px;
  }
  .operate-band h2 {
    font-weight: 400; font-size: 28px; line-height: 1.05; color: #fff;
  }
  .photo--meeting-small {
    left: 380px; top: 38px; width: 146px; height: 78px;
    background: linear-gradient(135deg, #8fa2a8 0%, #dfe3e0 60%, #5d6b6a 100%);
  }
  .operate-body {
    position: absolute; left: 40px; top: 160px; width: 486px;
    font-size: 10.5px; line-height: 1.8; color: var(--body-text);
  }
  .operate-body .drop-cap {
    float: left; font-size: 46px; line-height: 0.9;
    color: var(--brand-blue); font-weight: 400; margin: 2px 6px 0 0;
  }
  .operate-body .brand-name { color: var(--brand-blue); font-weight: 600; }
  .photo--advisor-couple {
    left: 50px; top: 385px; width: 290px; height: 200px;
    background: linear-gradient(135deg, #c7a98a 0%, #e6dccf 50%, #7d8ea8 100%);
  }
  .photo--retired-couple {
    left: 310px; top: 330px; width: 220px; height: 175px;
    background: linear-gradient(135deg, #e8d9d2 0%, #c9b3a6 55%, #5a5f70 100%);
    border: 4px solid var(--paper);
  }
  .brand-mark {
    position: absolute; right: 40px; bottom: 90px;
    display: flex; align-items: center; gap: 10px;
  }
  .brand-mark .brand-lockup {
    font-weight: 700; font-size: 22px; line-height: 1;
    color: var(--brand-navy); text-align: right;
  }
  .brand-mark .brand-dot {
    width: 18px; height: 18px; background: var(--brand-blue);
  }
</style>
</head>
<body>
  <main class="spread">
    <section class="page page--left">
      <div class="photo photo--family" role="img" aria-label="Photo of a smiling family of four embracing"></div>

      <header class="welcome-title">
        <h1>Welcome note</h1>
        <div class="brand-lockup">morvan<br>financial</div>
      </header>

      <div class="welcome-body">
        <p>Thank you for taking the time to consider MORVAN Financial as advisers to guide you in the planning of your financial future.</p>
        <div class="photo--handshake" role="img" aria-label="Photo of an adviser shaking hands with a client"></div>
        <p>At <span class="brand-name">MORVAN Financial</span>, our clients are individuals, each with unique lifestyle plans and aspirations. We consider ourselves highly fortunate and privileged to be able to share this important personal financial journey with you. At the foundation of this journey sits the relationship between you, as our client, and us, your financial advisers.</p>
        <p>This in turn forms a relationship based and built on communication, transparency and pro-activity. Once we have developed true understanding, we strive to structure tailored advice that explains and educates within an appropriate advice framework that provides certainty. Our aim is to empower you so that you control your financial situation, guided by our knowledge and expertise.</p>
        <p>We invite you to get to know us a little better in the following pages.</p>
      </div>
    </section>

    <section class="page page--right">
      <div class="operate-band">
        <h2>How do we<br>operate?</h2>
      </div>
      <div class="photo photo--meeting-small" role="img" aria-label="Photo of advisers meeting around a table"></div>

      <div class="operate-body">
        <p><span class="drop-cap">M</span><span class="brand-name">ORVAN Financial</span> is an independent, fee-for-advice, privately owned financial planning firm which was established in 2006. Within MORVAN, we value honesty, integrity and certainty. The advice and guidance we deliver is always based on your needs, free of product bias or commissions. Our planners are qualified and regularly trained, and we hold ourselves to the highest ethical standards. We work closely with accountants, solicitors and lenders so that every part of your plan fits together. Through regular reviews we keep you on track as your life changes, and we measure our success by the progress of the clients we serve.</p>
      </div>

      <div class="photo photo--advisor-couple" role="img" aria-label="Photo of a couple meeting with a financial adviser"></div>
      <div class="photo photo--retired-couple" role="img" aria-label="Photo of a retired couple reviewing plans with an adviser"></div>

      <div class="brand-mark">
        <div class="brand-lockup">MORVAN<br>financial</div>
        <div class="brand-dot"></div>
      </div>
    </section>
  </main>
</body>
</html>
```